Book Cover for Adult Coloring Book

I'd like a unique book cover design for a coloring book we are making for adults. The book cover is for an 8.5"x11" book. I need both the front and back cover created. We will want to include some text about the book on the back cover so there should be room for that. It will be less than 100 words.

1) The title is:

Grown-Up Sketch Pages: Cheeky Remarks Guaranteed To Leave Everyone Snorting Tea

2) A swear word may appear on the cover, however it should similar to some of the examples included.

3) I'd prefer the background be in black or white so that the picture and color "pop" off the page more.

I've included 4 example covers that I really like. Something similar to these is preferred.

Reason: I've had a designer ask if we could extend the deadline. I'd like to get as many options as possible since this is a guaranteed project. Please extend it to Friday, February 19th, 2016. I may choose someone before then, but I'd like to see as many as possible before I do. Thank you, Marcus

Target Market(s)

Adults 25-65

Industry/Entity Type

Publishing Company

Font styles to use
Sans Serif
Decorative
Script

Requirements
Must have
• Unique design and be colorful. It's okay to have a swear word but it should be subtle and similar in design to some of the examples I provided.
Nice to have
• Black or white background that will allow the image/text to "pop" on the page.
Should not have
• No slurs, racial or homophobic words.

```html
<!DOCTYPE html>
<html lang="en">
<head>
<meta charset="utf-8">
<title>Grown-Up Sketch Pages: Cheeky Remarks Guaranteed To Leave Everyone Snorting Tea</title>
<link rel="stylesheet" href="https://fonts.googleapis.com/css2?family=Great+Vibes&family=Rammetto+One&display=swap">
<style>
  :root {
    --ink: #000000;
    --smoke-blue: #1f6cff;
    --smoke-green: #3ee06a;
    --smoke-yellow: #f5e23a;
    --smoke-red: #ff3b2a;
    --violet: #5a2a8c;
    --glow: #fff6d8;
    --vine: #c9c6a8;
    --heart: #ff1a1a;
    --star: #d9a94a;
    --title-blue: #2fc4ee;
    --title-red: #e0332b;
    --title-gold: #f2c94c;
    --script-pink: #ff6fd8;
    --script-yellow: #f7ef4a;
    --script-green: #6bf06a;
    --script-cyan: #4fd7ff;
  }
  html, body {
    margin: 0;
    padding: 0;
    width: 927px;
    height: 1200px;
    overflow: hidden;
    background: var(--ink);
  }
  .cover {
    position: relative;
    width: 927px;
    height: 1200px;
    overflow: hidden;
    background:
      radial-gradient(ellipse 260px 360px at 470px 600px, rgba(120, 60, 190, 0.55), transparent 75%),
      var(--ink);
  }
  .art { position: absolute; }
  .smoke-left {
    left: 0; top: 0; width: 210px; height: 1200px;
    background: linear-gradient(180deg,
      rgba(31,108,255,0.75) 0%, rgba(62,224,106,0.7) 35%,
      rgba(245,226,58,0.65) 55%, rgba(255,120,40,0.7) 75%, rgba(255,59,42,0.6) 100%);
    filter: blur(18px);
    opacity: 0.7;
  }
  .smoke-right {
    right: 0; top: 0; width: 190px; height: 930px;
    background: linear-gradient(180deg, rgba(230,230,255,0.8), rgba(31,108,255,0.8) 45%, rgba(20,30,160,0.6));
    filter: blur(20px);
    opacity: 0.7;
  }
  .glow-top {
    left: 430px; top: 0; width: 497px; height: 380px;
    background: radial-gradient(ellipse at 60% 30%, rgba(255,246,216,0.45), transparent 70%);
  }
  .roses-top {
    left: 0; top: 0; width: 380px; height: 260px;
    background: radial-gradient(ellipse at 35% 40%, rgba(120,230,60,0.85), rgba(250,200,40,0.6) 40%, rgba(150,40,220,0.35) 70%, transparent 85%);
    border-radius: 0 0 60% 0;
  }
  .roses-bottom {
    left: 590px; top: 880px; width: 337px; height: 320px;
    background: radial-gradient(ellipse at 55% 55%, rgba(40,220,200,0.8), rgba(60,80,255,0.7) 45%, rgba(200,40,220,0.45) 70%, transparent 88%);
    border-radius: 60% 0 0 0;
  }
  .scatter {
    left: 150px; top: 250px; width: 640px; height: 800px;
    background: radial-gradient(circle at 20% 15%, rgba(255,26,26,0.18), transparent 30%),
                radial-gradient(circle at 80% 80%, rgba(255,26,26,0.18), transparent 30%),
                radial-gradient(circle at 70% 20%, rgba(217,169,74,0.12), transparent 25%);
  }
  .frame {
    position: absolute;
    left: 52px; top: 156px;
    width: 844px; height: 888px;
  }
  .title {
    position: absolute;
    left: 0; right: 0; top: 0;
    margin: 0;
    text-align: center;
    font-weight: normal;
  }
  .title span { display: block; }
  .script {
    font-family: "Great Vibes", cursive;
    background: linear-gradient(90deg, var(--script-pink), var(--script-yellow) 35%, var(--script-green) 65%, var(--script-cyan));
    -webkit-background-clip: text;
    background-clip: text;
    color: transparent;
    line-height: 1;
  }
  .series { position: absolute; left: 0; right: 0; top: 362px; font-size: 58px; }
  .headline {
    position: absolute; left: 0; right: 0;
    font-family: "Rammetto One", sans-serif;
    font-size: 88px;
    line-height: 1;
    letter-spacing: 1px;
    background: repeating-linear-gradient(135deg, var(--title-blue) 0 14px, var(--title-red) 14px 26px, var(--title-gold) 26px 32px);
    -webkit-background-clip: text;
    background-clip: text;
    color: transparent;
    -webkit-text-stroke: 2px #f3e6b0;
  }
  .headline-one { top: 458px; }
  .headline-two { top: 598px; }
  .tagline { position: absolute; left: 0; right: 0; top: 730px; font-size: 56px; }
  .tagline-end { position: absolute; left: 0; right: 0; top: 820px; font-size: 60px; }
</style>
</head>
<body>
<main class="cover">
  <div class="art smoke-left" role="img" aria-label="Flowing rainbow smoke ribbons down the left edge"></div>
  <div class="art smoke-right" role="img" aria-label="Flowing blue and white smoke on the right edge"></div>
  <div class="art glow-top" role="img" aria-label="Glowing light streaks in the upper right"></div>
  <div class="art roses-top" role="img" aria-label="Cluster of rainbow-coloured roses in the top left corner"></div>
  <div class="art roses-bottom" role="img" aria-label="Cluster of rainbow-coloured roses in the bottom right corner"></div>
  <div class="art scatter" role="img" aria-label="Scattered red hearts and gold stars across the black background"></div>

  <svg class="frame" viewBox="0 0 844 888" aria-hidden="true">
    <rect x="6" y="6" width="832" height="876" rx="60" ry="60" fill="none" stroke="var(--vine)" stroke-width="4"/>
    <rect x="18" y="18" width="808" height="852" rx="50" ry="50" fill="none" stroke="var(--vine)" stroke-width="1.5" opacity="0.6"/>
  </svg>

  <h1 class="title">
    <span class="script series">Grown-Up Sketch Pages</span>
    <span class="headline headline-one">CHEEKY</span>
    <span class="headline headline-two">REMARKS</span>
    <span class="script tagline">Guaranteed To Leave</span>
    <span class="script tagline-end">Everyone Snorting Tea</span>
  </h1>
</main>
</body>
</html>
```